Real Estate Office Front Facade Redesign - ideas needed

Kindly read this brief thoroughly as there are 2 deliverables:
1. Office building façade redesign (see attached logo and also photo of our office building façade)
2. I also require a design for a freestanding signboard that will be coordinated with the design of the office front please see the images attached labelled signboard.

Deliverable number 1:
I am looking for a minimalist contemporary design with strong colours to draw the attention of the passing Traffic.

The office facade is to be repainted so you may choose to recolour the office in any way to coordinate with logo however the attached logo must remain as is. I prefer the colours red black and white or shades of these colours.

Vireo property managers is a new company looking to target property investors in the local area. Most of our clients are from a middle to upper income demographic. We help these investors to rent out their properties and ensure they are maintained in good condition and provide a regular income.

The area we operate in is centrally located and close to the central business district of Perth.

Our office is situated in a residential area on a busy road facing diagonally at 45° down the road. People see our office from their cars whilst driving to work, there is no pedestrian traffic in the area. Therefore the office façade needs to stand out and any signage must be read by quickly passing traffic or convey our brand in seconds. Whilst the view of the office from the road is obscured somewhat by trees from a distance, once within 50 to 100 m of the office the full face of the office front is visible facing directly at the driver.

No measurements are provided for the façade of the office (please see the photo provided), this is a blank canvas as the whole building will be repainted to fit in with YOUR design. A logo is also attached. The colours red black and white are preferred.

Please provide an image of the office with signage/colours superimposed.

Deliverable number 2:
Also attached is an image of a freestanding sign for which I require a design. This sign is used for advertising properties for lease or sale which will be erected outside the front of residential houses. Again this sign needs to be bold and bright with a contemporary design. It needs to stand out from the crowd of many other signs in the area, whilst the sign advertises the property it must also promote our company brand by having a prominent logo. The size of these signboards will either be 1250 mm x 900 mm or 1800 mm x 625 mm. Please note that this sign must be rectangular in shape and cannot have any text or logo protruding outside of the lines of the rectangular sign due to cost restrictions.

Target Market(s)

Industry/Entity Type

Real Estate

Font styles to use
Sans Serif

Colors
ec1f27
ffffff
000000

Requirements
Must have
• Contemporary uncluttered design using the colours red black and white of shades of.
Nice to have
• A prominent logo with the words "Property Managers" easily read by passing traffic.
• Files provided with editable text and the name of the font used.
Should not have
• designs protruding outside of the overall building facia or sign rectangle.

```html
<!DOCTYPE html>
<html lang="en">
<head>
<meta charset="utf-8">
<title>Vireo Property Managers – For Lease or Sale Signboard</title>
<link rel="stylesheet" href="https://fonts.googleapis.com/css2?family=Alegreya+Sans:wght@400;500&display=swap">
<style>
  :root {
    --brand-red: #ec1f27;
    --ink: #1c1c1c;
    --panel: #eaf4f4;
    --white: #ffffff;
    --backdrop: #e6e8ea;
  }
  * { margin: 0; padding: 0; box-sizing: border-box; }
  html, body {
    width: 1200px;
    height: 799px;
    overflow: hidden;
    background: var(--backdrop);
  }
  .signboard {
    position: absolute;
    left: 92px;
    top: 20px;
    width: 1016px;
    height: 760px;
    background: var(--brand-red);
    padding: 14px;
    display: flex;
    flex-direction: column;
    font-family: "Alegreya Sans", sans-serif;
  }
  .brand-panel {
    height: 250px;
    background: var(--panel);
    border-radius: 16px 16px 0 0;
    display: flex;
    flex-direction: column;
    align-items: center;
    justify-content: center;
  }
  .brand-mark {
    width: 62px;
    height: 62px;
    background: var(--brand-red);
    margin-bottom: 18px;
  }
  .brand-name {
    font-size: 58px;
    font-weight: 400;
    letter-spacing: 8px;
    line-height: 1;
    color: var(--ink);
    text-transform: uppercase;
    padding-left: 8px;
  }
  .brand-tagline {
    margin-top: 8px;
    font-size: 15px;
    font-weight: 400;
    letter-spacing: 2px;
    color: var(--ink);
    text-transform: uppercase;
  }
  .offer-band {
    height: 207px;
    display: flex;
    align-items: center;
    justify-content: center;
  }
  .offer-title {
    color: var(--white);
    font-size: 128px;
    font-weight: 500;
    line-height: 1;
    letter-spacing: 1px;
  }
  .contact-panel {
    flex: 1;
    background: var(--panel);
    border-radius: 0 0 16px 16px;
    display: flex;
    flex-direction: column;
    align-items: center;
    justify-content: center;
    color: var(--ink);
    font-size: 44px;
    line-height: 60px;
    letter-spacing: 1px;
  }
</style>
</head>
<body>
  <div class="signboard">
    <div class="brand-panel">
      <div class="brand-mark"></div>
      <div class="brand-name">Vireo</div>
      <div class="brand-tagline">Property Managers</div>
    </div>
    <div class="offer-band">
      <h1 class="offer-title">For Lease or Sale</h1>
    </div>
    <div class="contact-panel">
      <p class="contact-line">Mobile 0411 2222 3333</p>
      <p class="contact-line">Office 9388 4444</p>
      <p class="contact-line">www.vireoproperty.com.au</p>
    </div>
  </div>
</body>
</html>
```